Tatami Hall Sport promotional leaflet to attract new members

We are looking to produce a leaflet for a local judo club to attract seniors and juniors 5+ the leaflet needs to encourage people to attend classes and train in the martial art

Tatami Hall Sport are proud members of the KSB UK (mats for every) and practice traditional judo which mean we wear white Gi's to show cleanliness and tradition.

www.tatamihallsport.co.uk

Target Market(s)

Kids from 5+ and Adults

Font styles to use
Serif

Requirements
Must have
• Must include times of training and how to book onto a beginners induction
• it must look enticing and show that Judo is fun for all
• must highlight we open on Tuesdays and Thursdays
• Juniors are from 6.15pm to 7.15pm
• seniors 7.30pm to 9pm
• classes are held at Vantrel Gym, Unit 7, Marlow Row, Denholm Close, Rustington, West Sussex, BN17 8QT
• We practice on a Sprung floor Mat area and is great for men and women
• first two classes free
Nice to have
• Classes are run by an expeirnced team including
• Dan Merrow 5th Dan and international referee
• Luke Merrow 2nd Dan current Global Grappling Union European Champion

```html
<!DOCTYPE html>
<html lang="en">
<head>
<meta charset="utf-8">
<title>Tatami Hall Sport – Leaflet</title>
<link rel="stylesheet" href="https://fonts.googleapis.com/css2?family=Bebas+Neue&family=Montserrat:wght@500;700&family=Roboto:wght@400;700&display=swap">
<style>
  :root {
    --backdrop: #f9e6ba;
    --paper: #ffffff;
    --red: #b31f27;
    --navy: #282b39;
    --wall: #4f5360;
    --wall-light: #7d808b;
    --gi: #ece8e2;
    --mat: #d8473f;
    --white: #ffffff;
  }
  html, body {
    margin: 0;
    padding: 0;
    width: 1015px;
    height: 1200px;
    overflow: hidden;
    background: var(--backdrop);
  }
  .leaflet {
    position: absolute;
    left: 92px;
    top: 20px;
    width: 830px;
    height: 1159px;
    display: block;
  }
  .brand-name { font-family: "Montserrat", sans-serif; font-weight: 500; font-size: 40px; fill: var(--navy); }
  .headline { font-family: "Bebas Neue", sans-serif; font-size: 94px; fill: var(--navy); letter-spacing: 4px; }
  .tagline { font-family: "Bebas Neue", sans-serif; font-size: 50px; fill: var(--navy); letter-spacing: 2px; }
  .tagline .accent { fill: var(--red); }
  .open-title { font-family: "Montserrat", sans-serif; font-weight: 700; font-size: 55px; fill: var(--navy); }
  .open-days { font-family: "Montserrat", sans-serif; font-weight: 500; font-size: 38px; fill: var(--red); letter-spacing: 1.5px; }
  .session-times { font-family: "Montserrat", sans-serif; font-weight: 700; font-size: 25px; fill: var(--navy); }
  .info-item { font-family: "Roboto", sans-serif; font-size: 25px; fill: var(--navy); letter-spacing: 0.5px; }
  .team-item { font-family: "Roboto", sans-serif; font-size: 21px; fill: var(--white); letter-spacing: 0.5px; }
  .site-url { font-family: "Roboto", sans-serif; font-weight: 700; font-size: 22px; fill: var(--white); }
</style>
</head>
<body>
<svg class="leaflet" viewBox="0 0 1145 1599" xmlns="http://www.w3.org/2000/svg">
  <defs>
    <linearGradient id="coachTone" x1="0" y1="0" x2="0.4" y2="1">
      <stop offset="0" stop-color="var(--wall)"/>
      <stop offset="0.45" stop-color="var(--wall-light)"/>
      <stop offset="0.75" stop-color="var(--gi)"/>
      <stop offset="1" stop-color="#c9ccd0"/>
    </linearGradient>
    <linearGradient id="groupTone" x1="0" y1="0" x2="0" y2="1">
      <stop offset="0" stop-color="var(--wall)"/>
      <stop offset="0.38" stop-color="var(--wall-light)"/>
      <stop offset="0.55" stop-color="var(--gi)"/>
      <stop offset="0.78" stop-color="var(--gi)"/>
      <stop offset="0.86" stop-color="var(--mat)"/>
      <stop offset="1" stop-color="var(--mat)"/>
    </linearGradient>
  </defs>

  <rect class="paper" x="0" y="0" width="1145" height="1599" fill="var(--paper)"/>

  <!-- brand -->
  <g class="brand">
    <circle cx="80" cy="127" r="28" fill="var(--red)"/>
    <text class="brand-name" x="122" y="142">Tatami Hall Sport</text>
  </g>

  <!-- headline -->
  <text class="headline" x="1062" y="236" text-anchor="end">A CLUB SETUP</text>
  <text class="tagline" x="1058" y="302" text-anchor="end">BY <tspan class="accent">JUDOKAS</tspan> FOR <tspan class="accent">JUDOKAS</tspan></text>

  <!-- photo collage -->
  <polygon class="photo photo-coach" role="img" aria-label="Photo: coach in a white gi smiling with two junior judoka in the dojo"
           points="0,252 640,500 640,560 110,785 0,742" fill="url(#coachTone)"/>
  <polygon class="photo photo-group" role="img" aria-label="Photo: smiling club members of all ages in white gis lined up on the red and grey mats"
           points="120,777 700,540 1145,400 1145,1157 405,887" fill="url(#groupTone)"/>

  <!-- graphic bands -->
  <polygon class="band band-navy" points="0,173 538,387 538,402 0,188" fill="var(--navy)"/>
  <polygon class="band band-red" points="0,203 640,450 640,496 0,250" fill="var(--red)"/>
  <polygon class="band band-red" points="875,470 1145,364 1145,392 880,498" fill="var(--red)"/>
  <polygon class="band band-red" points="95,775 650,545 660,568 125,790" fill="var(--red)"/>
  <polygon class="band band-white" points="0,742 110,785 120,790 0,746" fill="var(--white)"/>
  <polygon class="band band-red" points="0,752 372,890 0,890" fill="var(--red)"/>
  <polygon class="band band-red" points="405,887 1145,1157 1145,1237 405,947" fill="var(--red)"/>
  <polygon class="band band-white" points="405,894 1145,1164 1145,1172 405,902" fill="var(--white)"/>

  <!-- emblem circle -->
  <circle cx="750" cy="505" r="130" fill="var(--white)"/>
  <circle cx="750" cy="505" r="118" fill="var(--red)"/>

  <!-- opening info -->
  <text class="open-title" x="55" y="1047">WE OPEN ON</text>
  <text class="open-days" x="55" y="1102">TUESDAYS AND THURSDAYS</text>
  <text class="session-times" x="82" y="1148">Juniors 6.15pm - 7.15pm and Seniors 7.30pm - 9pm</text>

  <g class="info-list">
    <rect x="58" y="1206" width="18" height="18" fill="var(--navy)"/>
    <text class="info-item" x="84" y="1224">Classes are held at Vantrel Gym, Unit 7, Marlow Row, Denholm</text>
    <text class="info-item" x="84" y="1258">Close, Rustington, West Sussex, BN17 8QT</text>
    <rect x="58" y="1293" width="18" height="18" fill="var(--navy)"/>
    <text class="info-item" x="84" y="1311">We practice on a Sprung floor Mat area and is great for men and women</text>
    <rect x="58" y="1346" width="18" height="18" fill="var(--navy)"/>
    <text class="info-item" x="84" y="1364">First two classes are free – book your beginners induction online</text>
  </g>

  <!-- team footer -->
  <rect class="footer" x="0" y="1405" width="1145" height="168" fill="var(--navy)"/>
  <g class="team-list">
    <circle cx="67" cy="1438" r="7" fill="var(--white)"/>
    <text class="team-item" x="84" y="1445">Classes are run by an experienced team including</text>
    <circle cx="67" cy="1473" r="7" fill="var(--white)"/>
    <text class="team-item" x="84" y="1480">Dan Merrow 5th Dan and international referee</text>
    <circle cx="67" cy="1510" r="7" fill="var(--white)"/>
    <text class="team-item" x="84" y="1517">Luke Merrow 2nd Dan current Global Grappling Union European Champion</text>
  </g>
  <text class="site-url" x="573" y="1560" text-anchor="middle">www.tatamihallsport.co.uk</text>

  <!-- base strip -->
  <rect x="0" y="1573" width="405" height="26" fill="var(--white)"/>
  <rect x="405" y="1573" width="353" height="26" fill="var(--red)"/>
  <rect x="758" y="1573" width="387" height="26" fill="var(--navy)"/>
</svg>
</body>
</html>
```